P&H RESTORATION

I want a brochure similiar to the example i've attached.
My company name is P&H Restoration. The website is: P-H-Restoration.com.
The phone number is 803.417.9056.

I don't like the "yellow" being the main color of the example so I'm open to suggestions. I want something CLEAN & Simple, like our logo . This will be a bi fold brochure

```html
<!DOCTYPE html>
<html lang="en">
<head>
<meta charset="utf-8">
<title>P&amp;H Restoration – Bi-fold Brochure</title>
<link rel="stylesheet" href="https://fonts.googleapis.com/css2?family=Bebas+Neue&family=Montserrat:ital,wght@0,400;0,500;1,800&display=swap">
<style>
  :root{
    --teal:#087b7f;
    --ink:#0b0b0b;
    --paper:#ffffff;
    --backdrop:#cdcccd;
    --mist:#e9eaeb;
    --head:"Bebas Neue", "Arial Narrow", sans-serif;
    --body:"Montserrat", Arial, sans-serif;
  }
  *{margin:0;padding:0;box-sizing:border-box}
  html,body{width:749px;height:1200px;overflow:hidden;background:var(--backdrop)}
  .canvas{position:relative;width:749px;height:1200px}
  .spread{position:absolute;left:61px;width:626px;height:484px;background:var(--paper);display:flex}
  .spread--outside{top:82px}
  .spread--inside{top:624px}
  .panel{position:relative;width:313px;height:484px;overflow:hidden}
  .panel svg.shapes{position:absolute;inset:0;width:313px;height:484px}
  .panel--cover{background:linear-gradient(90deg,#d6d7d8 0%,#f7f7f7 45%,#fff 100%)}
  .panel--photo{background:var(--mist)}
  .head{position:absolute;font-family:var(--head);line-height:.92;color:var(--ink);white-space:nowrap}
  .teal{color:var(--teal)}
  .claim{left:27px;top:200px;font-size:36px}
  .team{position:absolute;left:28px;top:236px;font-family:var(--body);font-style:italic;font-weight:800;font-size:33px;line-height:1.17;color:var(--teal);white-space:nowrap}
  .call{position:absolute;right:30px;top:418px;text-align:right}
  .call__label{font-family:var(--head);font-size:20px;color:var(--teal);line-height:1}
  .call__phone{font-family:var(--head);font-size:30px;color:var(--ink);line-height:1;letter-spacing:.3px}
  .brand{position:absolute;left:25px;top:41px;width:114px;height:47px;border:1px solid var(--ink);display:flex;align-items:center;justify-content:center;font-family:var(--body);font-weight:500;font-size:13px;color:var(--ink);background:transparent}
  .stack{position:absolute;font-family:var(--head);line-height:1.08;white-space:nowrap}
  .stack--cover{left:26px;top:110px;font-size:57px}
  .stack--back{right:24px;top:80px;font-size:49px;text-align:right;line-height:.9}
  .damage{position:absolute;left:33px;top:262px;font-family:var(--head);color:var(--ink);line-height:.9;white-space:nowrap}
  .damage__l1{font-size:44px}
  .damage__l2{font-size:50px}
  .damage__sub{font-size:18px;color:var(--teal);line-height:1;margin-top:6px;margin-left:2px}
  .features{position:absolute;left:20px;top:378px;width:280px;display:grid;grid-template-columns:130px 145px;column-gap:0;row-gap:10px}
  .feature__title{display:flex;align-items:center;gap:4px;font-family:var(--head);font-size:14px;line-height:1;color:var(--ink)}
  .feature__title svg{width:8px;height:8px;flex:none}
  .feature__text{font-family:var(--body);font-size:4.4px;line-height:1.22;color:var(--ink);margin-top:2px;padding-left:12px}
</style>
</head>
<body>
<main class="canvas">

  <!-- Outside spread: back panel + front cover -->
  <section class="spread spread--outside">
    <div class="panel panel--back">
      <svg class="shapes" viewBox="0 0 313 484">
        <defs>
          <linearGradient id="siteTone" x1="0" y1="0" x2="1" y2="1">
            <stop offset="0" stop-color="#d9d4cc"/><stop offset=".6" stop-color="#bfb6a8"/><stop offset="1" stop-color="#8f8474"/>
          </linearGradient>
        </defs>
        <circle cx="171" cy="29" r="48" fill="var(--teal)"/>
        <g role="img" aria-label="Photo of a worker in a hard hat installing ceiling wiring on a renovation site">
          <circle cx="82" cy="94" r="94" fill="url(#siteTone)"/>
        </g>
        <circle cx="54" cy="373" r="49" fill="none" stroke="var(--teal)" stroke-width="1.6"/>
        <circle cx="25" cy="453" r="62" fill="none" stroke="var(--teal)" stroke-width="26"/>
      </svg>
      <h2 class="head claim">Insurance Claim?</h2>
      <p class="team">WE’RE On<br>YOUR TEAM</p>
      <div class="call">
        <div class="call__label">Call Now!</div>
        <div class="call__phone">(803) 417 9056</div>
      </div>
    </div>

    <div class="panel panel--cover">
      <svg class="shapes" viewBox="0 0 313 484">
        <defs>
          <linearGradient id="kitchenTone" x1="0" y1="0" x2="0" y2="1">
            <stop offset="0" stop-color="#cfd6d8"/><stop offset=".45" stop-color="#b89f7f"/><stop offset=".7" stop-color="#e4e8ea"/><stop offset="1" stop-color="#2c3a44"/>
          </linearGradient>
        </defs>
        <circle cx="265" cy="29" r="67" fill="none" stroke="var(--teal)" stroke-width="30"/>
        <circle cx="319" cy="116" r="94" fill="none" stroke="var(--teal)" stroke-width="1.6"/>
        <circle cx="172" cy="453" r="126" fill="var(--teal)"/>
        <g role="img" aria-label="Photo of a modern kitchen with wooden cabinets and white chairs standing in flood water">
          <circle cx="126" cy="413" r="126" fill="url(#kitchenTone)"/>
        </g>
      </svg>
      <div class="brand">P&amp;H Restoration</div>
      <h1 class="stack stack--cover">
        <span>Build</span><br><span class="teal">Renovate</span><br><span>Restore</span>
      </h1>
    </div>
  </section>

  <!-- Inside spread -->
  <section class="spread spread--inside">
    <div class="panel panel--services">
      <svg class="shapes" viewBox="0 0 313 484">
        <defs>
          <linearGradient id="planTone" x1="0" y1="0" x2="1" y2="1">
            <stop offset="0" stop-color="#e6eef9"/><stop offset=".6" stop-color="#b9cde8"/><stop offset="1" stop-color="#8fadd6"/>
          </linearGradient>
        </defs>
        <circle cx="152" cy="37" r="57" fill="var(--teal)"/>
        <g role="img" aria-label="Photo of rolled architectural blueprints">
          <circle cx="225" cy="94" r="114" fill="url(#planTone)"/>
        </g>
        <circle cx="268" cy="254" r="37" fill="none" stroke="var(--teal)" stroke-width="1.6"/>
        <circle cx="320" cy="283" r="41" fill="none" stroke="var(--teal)" stroke-width="17"/>
        <g class="icon-house" fill="var(--ink)">
          <path d="M33 208 L58 190 L84 208 L81 212 L58 195 L36 212 Z"/>
          <rect x="72" y="190" width="6" height="10"/>
          <path d="M40 210 L58 197 L77 210 L77 238 L40 238 Z"/>
          <path d="M58 206 C55 212 53 215 53 218 A5 5 0 0 0 63 218 C63 215 61 212 58 206 Z" fill="#fff"/>
          <path d="M67 214 C65 218 64 220 64 222 A3.5 3.5 0 0 0 71 222 C71 220 70 218 67 214 Z" fill="#fff"/>
          <circle cx="38" cy="229" r="2"/><circle cx="35" cy="234" r="1.5"/><circle cx="41" cy="236" r="1.6"/>
        </g>
      </svg>
      <h2 class="damage">
        <span class="damage__l1">Water <span class="teal">or</span></span><br>
        <span class="damage__l2">Mold Damage?</span>
        <div class="damage__sub">What happens after the cleanup?</div>
      </h2>
      <div class="features">
        <div class="feature">
          <h3 class="feature__title"><svg viewBox="0 0 8 8"><path d="M1 1h5v2H4v2H3V3H1z" fill="var(--teal)"/><circle cx="3.5" cy="7" r="1" fill="var(--teal)"/></svg>Adjuster’s Inspection</h3>
          <p class="feature__text">Feel confident. Be sure you received a fair and accurate assessment &amp; repair of all damages with our team’s use of industry leading estimating systems and On-Site Review.</p>
        </div>
        <div class="feature">
          <h3 class="feature__title"><svg viewBox="0 0 8 8"><path d="M1 1l6 6M7 1L1 7" stroke="var(--teal)" stroke-width="1.4"/></svg>Superior Craftsmanship</h3>
          <p class="feature__text">Don’t settle for satisfactory. Our team is committed to the highest standards of excellence every step of the way. Trust us when we say that we’ll make your smile.</p>
        </div>
        <div class="feature">
          <h3 class="feature__title"><svg viewBox="0 0 8 8"><path d="M1 0h6v1H6L4 4l2 3h1v1H1V7h1l2-3-2-3H1z" fill="var(--teal)"/></svg>Timely Settlement</h3>
          <p class="feature__text">Don’t wait. Minimize the hassle of long processing times from estimate to settlement when you team up with an Insurance Repair Specialist.</p>
        </div>
        <div class="feature">
          <h3 class="feature__title"><svg viewBox="0 0 8 8"><path d="M0 4L4 0l4 4H7v4H1V4z" fill="var(--teal)"/></svg>Under One Roof</h3>
          <p class="feature__text">Don’t worry. You won’t need to arrange meetings with multiple contractors. We’ll take care of everything from demo to final cleanup.</p>
        </div>
      </div>
    </div>

    <div class="panel panel--photo">
      <svg class="shapes" viewBox="0 0 313 484">
        <defs>
          <linearGradient id="workerTone" x1="0" y1="0" x2="1" y2="1">
            <stop offset="0" stop-color="#d7d8d9"/><stop offset=".5" stop-color="#c6c7c8"/><stop offset="1" stop-color="#eeeeee"/>
          </linearGradient>
        </defs>
        <g role="img" aria-label="Faded photo of two workers on a ladder fitting a ceiling in a bright room">
          <rect width="313" height="484" fill="url(#workerTone)"/>
        </g>
        <circle cx="247" cy="264" r="38" fill="none" stroke="var(--teal)" stroke-width="1.6"/>
        <circle cx="313" cy="292" r="52" fill="none" stroke="var(--teal)" stroke-width="20"/>
        <circle cx="86" cy="466" r="77" fill="none" stroke="var(--teal)" stroke-width="25" opacity=".8"/>
        <circle cx="116" cy="407" r="50" fill="none" stroke="var(--teal)" stroke-width="1.6"/>
      </svg>
      <h2 class="stack stack--back">
        <span>Build</span><br><span class="teal">Renovate</span><br><span>Restore</span>
      </h2>
    </div>
  </section>

</main>
</body>
</html>
```